Business Card Makeover. Recreate a sleek modern design for our business card.

DO NOT COPY OUR CURRENT DESIGN. MUST BE ONE SIDED BUSINESS CARD.
Create a new business card design, using our new logo. Attached is a sample of our current design and new logo. Please note the address and email will change. The new address is 417 Corvell West Palm Beach 33472 and our website will be www.talvendrake.example.

We are an architectural and interior design firm. We prefer a clean modern look. Something that is refined and emulates excellence.

Industry/Entity Type

Architecture

Contact Information for Business Card

clean modern look, please do not copy our attached design.

Font styles to use
Other font styles liked:
• see attached business card font

Colors

Designer to choose colors to be used in the design.

Requirements
Must have
• Must have a modern appeal and resemble our current branding.
Nice to have
• modern font, our logo, legible name and titles progressive design
Should not have
• Do not add colors not reflected in our branding. Should not look like our current card.

```html
<!DOCTYPE html>
<html lang="en">
<head>
<meta charset="utf-8">
<title>Talvendrake + Partners — Business Cards</title>
<link rel="stylesheet" href="https://fonts.googleapis.com/css2?family=Playfair+Display:wght@400&family=Montserrat:wght@400&display=swap">
<style>
  :root {
    --backdrop: #d8cdbd;
    --card: #ffffff;
    --ink: #1c1c1c;
    --text-grey: #666a6e;
    --soft-grey: #e6e6e7;
    --brand-blue: #1f55a6;
  }
  * { box-sizing: border-box; margin: 0; padding: 0; }
  html, body { width: 1200px; height: 900px; overflow: hidden; }
  body {
    background: var(--backdrop);
    position: relative;
    font-family: "Montserrat", Arial, sans-serif;
  }
  .card {
    position: absolute;
    left: 311px;
    width: 578px;
    height: 330px;
    background: var(--card);
    overflow: hidden;
  }
  .card--first { top: 98px; }
  .card--second { top: 472px; }

  .accent-rule {
    position: absolute; left: 28px; top: 0;
    width: 3px; height: 72px; background: var(--brand-blue);
  }
  .tagline {
    position: absolute; left: 20px; bottom: 36px;
    transform-origin: left bottom;
    transform: rotate(-90deg) translateY(100%);
    font-family: "Playfair Display", Georgia, serif;
    font-size: 15px; letter-spacing: 0.6px;
    color: var(--text-grey); white-space: nowrap;
  }
  .backdrop-disc {
    position: absolute; left: 58px; top: 26px;
    width: 204px; height: 204px; border-radius: 50%;
    background: var(--soft-grey); opacity: 0.55;
  }
  .wordmark {
    position: absolute; right: 36px; top: 31px; text-align: right;
    font-family: "Playfair Display", Georgia, serif;
    color: var(--ink); line-height: 1;
  }
  .wordmark__name { font-size: 24px; letter-spacing: 0.5px; }
  .wordmark__sub { font-size: 8px; letter-spacing: 2.4px; margin-top: 3px; }

  .identity {
    position: absolute; right: 56px; text-align: right;
  }
  .identity::after {
    content: ""; position: absolute; right: -17px; top: 0;
    width: 3px; height: 28px; background: var(--brand-blue);
  }
  .identity__name {
    font-family: "Playfair Display", Georgia, serif;
    font-size: 15.5px; letter-spacing: 1.2px; color: var(--ink);
    line-height: 18px; text-transform: uppercase;
  }
  .identity__role { font-size: 13.5px; color: var(--brand-blue); line-height: 16px; }

  .contacts {
    position: absolute; right: 32px; list-style: none;
  }
  .contacts li {
    display: flex; justify-content: flex-end; align-items: center;
    height: 20.6px; font-size: 14.5px; color: var(--text-grey);
  }
  .contacts svg { width: 15px; height: 15px; margin-left: 9px; fill: var(--brand-blue); }

  .address {
    position: absolute; left: 58px; top: 241px;
    font-size: 14px; line-height: 19.5px; color: var(--text-grey);
    font-style: normal;
  }
  .address__licence { color: var(--brand-blue); }
</style>
</head>
<body>
  <svg width="0" height="0" style="position:absolute" aria-hidden="true">
    <symbol id="icon-phone" viewBox="0 0 16 16"><path d="M3.5 1.5l2.3 2.6-1.2 1.8c.8 1.9 2.2 3.3 4.1 4.2l1.8-1.2 2.6 2.3-1.4 2.3C6.7 13.3 2.6 9.2 1.2 3.2z"/></symbol>
    <symbol id="icon-fax" viewBox="0 0 16 16"><path d="M1 4h3v11H1zM5 1h7l2 2v3H5zM5 7h10v8H5zm2 2v1.4h2V9zm3 0v1.4h2V9zm-3 2.6V13h2v-1.4zm3 0V13h2v-1.4z"/></symbol>
    <symbol id="icon-mail" viewBox="0 0 16 16"><path d="M1 3h14v1.2L8 9 1 4.2zm0 2.8l7 4.8 7-4.8V13H1z"/></symbol>
    <symbol id="icon-globe" viewBox="0 0 16 16"><path d="M8 1a7 7 0 100 14A7 7 0 008 1zm-.6 2.2c-.9.7-1.6 1.8-1.3 2.8.4 1.1 2 .8 2.4 1.9.3 1-.9 1.6-.6 2.8.2.8 1 1.4.6 2.2A5.1 5.1 0 013 8c0-2.5 1.9-4.5 4.4-4.8zm3.2.9A5 5 0 0113 8c0 1.3-.5 2.5-1.3 3.4-.3-1.1-1.3-1.3-1.6-2.3-.3-1 .8-1.7.3-2.7-.4-.8-1.3-.9-1.3-1.6 0-.3.3-.6.5-.7z"/></symbol>
    <symbol id="icon-mobile" viewBox="0 0 16 16"><path d="M4 1h8v14H4zm1.4 1.6v9.6h5.2V2.6zM7 13.2v.9h2v-.9z"/></symbol>
  </svg>

  <article class="card card--first">
    <span class="accent-rule"></span>
    <p class="tagline">architecture + interior design</p>
    <div class="backdrop-disc" role="img" aria-label="Faint brand symbol area"></div>
    <div class="wordmark">
      <div class="wordmark__name">TALVENDRAKE</div>
      <div class="wordmark__sub">+ PARTNERS</div>
    </div>
    <div class="identity" style="top:161px">
      <p class="identity__name">Marisa Ellwood, AIA, LEED® AP</p>
      <p class="identity__role">Partner | Director of Design</p>
    </div>
    <ul class="contacts" style="top:216px">
      <li>561 555 0144<svg><use href="#icon-phone"/></svg></li>
      <li>561 555 0178<svg><use href="#icon-fax"/></svg></li>
      <li>marisa@talvendrake.example<svg><use href="#icon-mail"/></svg></li>
      <li>www.talvendrake.example<svg><use href="#icon-globe"/></svg></li>
    </ul>
    <address class="address">
      417 Corvell<br>
      West Palm Beach, FL 33472<br>
      <span class="address__licence">LIC.# AA41180527</span>
    </address>
  </article>

  <article class="card card--second">
    <span class="accent-rule"></span>
    <p class="tagline">architecture + interior design</p>
    <div class="backdrop-disc" role="img" aria-label="Faint brand symbol area"></div>
    <div class="wordmark">
      <div class="wordmark__name">TALVENDRAKE</div>
      <div class="wordmark__sub">+ PARTNERS</div>
    </div>
    <div class="identity" style="top:145px">
      <p class="identity__name">Henry Alder</p>
      <p class="identity__role">Partner | Director of Design</p>
    </div>
    <ul class="contacts" style="top:192px">
      <li>561 555 0123<svg><use href="#icon-mobile"/></svg></li>
      <li>561 555 0144<svg><use href="#icon-phone"/></svg></li>
      <li>561 555 0178<svg><use href="#icon-fax"/></svg></li>
      <li>henry@talvendrake.example<svg><use href="#icon-mail"/></svg></li>
      <li>www.talvendrake.example<svg><use href="#icon-globe"/></svg></li>
    </ul>
    <address class="address">
      417 Corvell<br>
      West Palm Beach, FL 33472<br>
      <span class="address__licence">LIC.# AA41180527</span>
    </address>
  </article>
</body>
</html>
```